Etiketten-Design für Weinflasche
Helga hat mit sehr viel Mühe und Hingabe unsere Wünsche umgesetzt. Wir sind mit dem Endergebnis sehr zufrieden.
Zielgruppe
Wir sind ein Weingut-Startup und suchen ein frisches, hochwertiges Design für unsere Flaschenetiketten.
Aufgabenstellung
Wir benötigen ein Vorderetikett für unsere Weinflaschen mit folgenden Vorgaben:
- Etiketten sollen variabel nutzbar sein, für verschiedene Rebsorten bspw. in versch. Farben
- Auf dem Etikett zwingend: Logo (siehe Anlage), Rebsorte, Anbaugebiet (Nahe)
- Wiedererkennungswert
- nicht zu klassisch, nicht zu futuristisch (gutes Mittelmaß, wie beim Logo auch)
- ggf. Spiel mit (Hintergrund-)Farben für verschiedene Sorten, ggf. Hintergrundmuster (evtl. Höhenlinien des Talwiesers, Bad Kreuznach (unser Heimatberg))
- Anpassung an verschiedene Qualitätsstufen (Gutswein, Ortswein, Lagenwein), ggf. schwarzes Sonderetikett für absolutes Premiumsegment
- unsere Werte als Naturnah und familiengeführtes Weingut sollen transportiert werden
- Maß: 80x90mm (breitxhoch)
Insgesamt sind wir offen für verschiedene Vorschläge, auch wenn die Vorgaben oben teils sehr konkret sind. Bei guten Designs lassen wir uns gerne von unseren Vorstellungen abbringen ;)

```html
<!DOCTYPE html>
<html lang="de">
<head>
<meta charset="utf-8">
<title>Weinetikett Reserva – Weingut Lauven</title>
<link rel="stylesheet" href="https://fonts.googleapis.com/css2?family=Roboto+Condensed:wght@400;700&display=swap">
<style>
  :root {
    --page-bg: #e9e9eb;
    --label-bg: #ffffff;
    --gold: #a8893f;
    --vine-green: #6e7f2a;
    --leaf-tint-a: #f7f5ee;
    --leaf-tint-b: #efece0;
  }
  html, body {
    margin: 0;
    width: 1200px;
    height: 1200px;
    overflow: hidden;
    background: var(--page-bg);
  }
  .wine-label {
    position: absolute;
    left: 120px;
    top: 60px;
    width: 960px;
    height: 1080px;
    background: var(--label-bg);
    box-shadow: 0 2px 10px rgba(0,0,0,0.08);
    font-family: "Roboto Condensed", Arial, sans-serif;
  }
  .label-frame {
    position: absolute;
    inset: 0;
  }
  .region-badge {
    position: absolute;
    left: 377px;
    top: 52px;
    width: 208px;
    height: 68px;
    background: var(--gold);
    color: #fff;
    font-weight: 700;
    font-size: 40px;
    letter-spacing: 10px;
    display: flex;
    align-items: center;
    justify-content: center;
    padding-left: 10px;
    box-sizing: border-box;
  }
  .estate-name {
    position: absolute;
    left: 0;
    right: 0;
    top: 258px;
    text-align: center;
    color: var(--vine-green);
    font-weight: 400;
    font-size: 130px;
    line-height: 1;
  }
  .leaf-motif {
    position: absolute;
    left: 204px;
    top: 475px;
    width: 550px;
    height: 437px;
    border-radius: 46% 40% 30% 30%;
    background: radial-gradient(ellipse at 50% 55%, var(--leaf-tint-b), var(--leaf-tint-a) 70%, var(--label-bg));
  }
  .grape-variety {
    position: absolute;
    left: 0;
    right: 0;
    top: 925px;
    text-align: center;
    color: var(--gold);
    font-weight: 400;
    font-size: 76px;
    letter-spacing: 9px;
    line-height: 1;
    padding-left: 9px;
  }
</style>
</head>
<body>
  <main class="wine-label">
    <svg class="label-frame" width="960" height="1080" viewBox="0 0 960 1080" aria-hidden="true">
      <g stroke="var(--gold)" stroke-width="3" fill="none">
        <line x1="79" y1="87" x2="354" y2="87"/>
        <line x1="607" y1="87" x2="882" y2="87"/>
        <line x1="79" y1="87" x2="79" y2="1005"/>
        <line x1="882" y1="87" x2="882" y2="1005"/>
        <line x1="79" y1="1005" x2="281" y2="1005"/>
        <line x1="677" y1="1005" x2="882" y2="1005"/>
      </g>
    </svg>
    <div class="region-badge">NAHE</div>
    <div class="estate-name">Lauven</div>
    <div class="leaf-motif" role="img" aria-label="Zarte Strichzeichnung eines Weinblatts als heller Hintergrund"></div>
    <div class="grape-variety">RESERVA</div>
  </main>
</body>
</html>
```